Hollowmere Farm Promotional Leaflet

The team at Hollowmere Farm can help with every aspect of managing and enhancing your home from housekeeping and professional cleaning, laundry and ironing to providing chic and contemporary flower arrangements and even food for your pets!We take pride in providing high-end, consistent and reliable professional services bespoke to you. Whether you are a busy professional working long hours, a stay-at home parent or retired; having professional help in the home gives you time to spend on the things you enjoy.We are providing a very upmarket, highly professional service and need an A5 promotional leaflet to be designed. Please refer to www.hollowmerefarm-example.co.uk and see the section on 'Home Management'The leaflet should incorporate the Hollowmere Farm logo without the 'tipi', and any suitable photography images used on the home page of the website or the 'home management' section.

Target Market(s)

high-end, affluent owners of luxury homes

Industry/Entity Type

Farm

Contact Information for Business Card

The business card design needs to be suitable for use across all of Hollowmere Farm businesses, specifically:
Hollowmere Farm Home Management - otherwise known as Hollowmere Farm @ Home (this uses the typographical logo
Hollowmere Farm Weddings & Events - this uses the 'tipi' logo

Requirements
Must have
• Design in keeping with the look and feel of the logo and website design
• www.hollowmerefarm-example.co.uk

```html
<!DOCTYPE html>
<html lang="en">
<head>
<meta charset="utf-8">
<title>Hollowmere Farm Home Management Leaflet</title>
<link href="https://fonts.googleapis.com/css2?family=Tenor+Sans&family=Open+Sans:wght@400;600;700&display=swap" rel="stylesheet">
<style>
  :root {
    --pink: #d92f5e;
    --pink-light: #ef7bac;
    --gold: #e3b865;
    --charcoal: #454547;
    --white: #ffffff;
    --ink: #3a3a3c;
    --backdrop: #e9e6e2;
  }
  html, body {
    margin: 0;
    padding: 0;
    width: 1200px;
    height: 1000px;
    overflow: hidden;
    background: var(--backdrop);
  }
  .canvas {
    position: relative;
    width: 1200px;
    height: 1000px;
  }
  .leaflet {
    position: absolute;
    left: 55px;
    top: 116px;
    width: 1090px;
    height: 768px;
    background: var(--white);
    box-shadow: 0 2px 6px rgba(0,0,0,0.15);
    overflow: hidden;
  }

  /* Left panel */
  .panel-left {
    position: absolute;
    left: 0;
    top: 0;
    width: 508px;
    height: 768px;
    background: var(--charcoal);
  }
  .flowers-photo {
    position: absolute;
    left: 0;
    top: 0;
    width: 508px;
    height: 149px;
    background: linear-gradient(100deg, #6a3a3a 0%, #e9a9c6 25%, #f1c1d6 45%, #c9708f 60%, #f4eef0 78%, #3b2a2a 100%);
  }
  .brand-band {
    position: absolute;
    left: 0;
    top: 149px;
    width: 508px;
    height: 174px;
    background: var(--pink);
    text-align: center;
    color: var(--white);
  }
  .brand-name {
    position: absolute;
    left: 0;
    right: 0;
    top: 34px;
    margin: 0;
    font-family: "Tenor Sans", sans-serif;
    font-size: 50px;
    font-weight: 400;
    letter-spacing: 2px;
    color: var(--pink-light);
  }
  .brand-division {
    position: absolute;
    left: 0;
    right: 0;
    top: 126px;
    margin: 0;
    font-family: "Tenor Sans", sans-serif;
    font-size: 36px;
    letter-spacing: 1.5px;
    color: var(--white);
    font-weight: 400;
  }
  .promise {
    position: absolute;
    left: 33px;
    top: 357px;
    width: 450px;
    margin: 0;
    font-family: "Tenor Sans", sans-serif;
    font-size: 20px;
    line-height: 26px;
    letter-spacing: 1.2px;
    color: var(--white);
    font-weight: 400;
  }
  .intro {
    position: absolute;
    left: 34px;
    top: 467px;
    width: 445px;
    margin: 0;
    font-family: "Open Sans", sans-serif;
    font-size: 15px;
    line-height: 23px;
    color: var(--white);
    text-align: justify;
  }
  .assurances {
    position: absolute;
    left: 35px;
    top: 527px;
    width: 438px;
    height: 219px;
    border-collapse: collapse;
    table-layout: fixed;
  }
  .assurances td {
    border: 2px solid var(--white);
    width: 50%;
    height: 73px;
    text-align: center;
    vertical-align: middle;
    font-family: "Tenor Sans", sans-serif;
    font-size: 13px;
    line-height: 16px;
    letter-spacing: 0.5px;
    color: var(--white);
    padding: 0 14px;
  }

  /* Right panel */
  .panel-right {
    position: absolute;
    left: 508px;
    top: 0;
    width: 582px;
    height: 768px;
    background: var(--white);
    text-align: center;
    color: var(--ink);
  }
  .services-lead {
    position: absolute;
    left: 0;
    right: 0;
    top: 27px;
    margin: 0;
    font-family: "Open Sans", sans-serif;
    font-size: 13px;
  }
  .services-title {
    position: absolute;
    left: 0;
    right: 0;
    top: 43px;
    margin: 0;
    font-family: "Open Sans", sans-serif;
    font-size: 18.5px;
    font-weight: 700;
    letter-spacing: 0.3px;
  }
  .services-sub {
    position: absolute;
    left: 0;
    right: 0;
    top: 67px;
    margin: 0;
    font-family: "Open Sans", sans-serif;
    font-size: 13px;
  }
  .service-grid {
    position: absolute;
    left: 4px;
    top: 93px;
    width: 574px;
    display: grid;
    grid-template-columns: repeat(4, 140px);
    grid-template-rows: repeat(2, 140px);
    gap: 5px 4px;
  }
  .service-tile {
    display: flex;
    align-items: center;
    justify-content: center;
    padding: 0 8px;
    font-family: "Tenor Sans", sans-serif;
    font-size: 14px;
    line-height: 18px;
    letter-spacing: 0.6px;
    color: var(--white);
  }
  .service-tile--charcoal { background: var(--charcoal); }
  .service-tile--pink { background: var(--pink); }
  .service-tile--gold { background: var(--gold); color: var(--ink); }
  .service-tile--blush { background: var(--pink-light); }

  .wardrobe-photo {
    position: absolute;
    left: 0;
    top: 383px;
    width: 582px;
    height: 221px;
    background: linear-gradient(90deg, #6b4e3c 0%, #b89a85 22%, #d9cbbf 45%, #c9b3a2 60%, #8b6d58 82%, #5c4333 100%);
  }
  .coverage-band {
    position: absolute;
    left: 0;
    top: 609px;
    width: 582px;
    height: 60px;
    background: var(--pink);
    display: flex;
    align-items: center;
    justify-content: center;
    margin: 0;
    font-family: "Tenor Sans", sans-serif;
    font-size: 17.5px;
    line-height: 21px;
    letter-spacing: 1px;
    color: var(--white);
    font-weight: 400;
  }
  .contact {
    position: absolute;
    left: 0;
    right: 0;
    top: 680px;
    font-family: "Open Sans", sans-serif;
    color: var(--ink);
  }
  .contact-lead {
    margin: 0 0 2px;
    font-size: 14px;
  }
  .contact-lines {
    margin: 0;
    font-size: 16px;
    font-weight: 700;
    line-height: 25px;
  }
  .contact-divider {
    display: inline-block;
    margin: 0 12px;
    font-weight: 400;
  }
</style>
</head>
<body>
<div class="canvas">
  <article class="leaflet">
    <section class="panel-left">
      <div class="flowers-photo" role="img" aria-label="Photograph of a pink hydrangea, rose and lily flower arrangement"></div>
      <header class="brand-band">
        <p class="brand-name">Hollowmere Farm</p>
        <h1 class="brand-division">HOME MANAGEMENT</h1>
      </header>
      <h2 class="promise">WE TAKE PRIDE IN PROVIDING HIGH-END, CONSISTENT AND RELIABLE PROFESSIONAL SERVICES BESPOKE TO YOU</h2>
      <p class="intro">Coming home to a beautiful environment and being able to relax and enjoy your time is something we all deserve.</p>
      <table class="assurances">
        <tr>
          <td>SATISFACTION<br>GUARANTEED</td>
          <td>PROFESSIONAL STAFF<br>YOU CAN TRUST<br>AND RELY ON</td>
        </tr>
        <tr>
          <td>COMPETITIVE RATES</td>
          <td>CRB CHECKED<br>AND REFERENCED</td>
        </tr>
        <tr>
          <td>MEMBER OF<br>THE DOMESTIC<br>STAFFING<br>GUILD</td>
          <td>FULLY INSURED</td>
        </tr>
      </table>
    </section>

    <section class="panel-right">
      <p class="services-lead">The team at &nbsp;Hollowmere Farm can help with</p>
      <h2 class="services-title">EVERY ASPECT OF MANAGING AND ENHANCING YOUR HOME</h2>
      <p class="services-sub">including:</p>
      <div class="service-grid">
        <div class="service-tile service-tile--charcoal">REGULAR<br>HOUSEKEEPING<br>AND<br>PROFESSIONAL<br>CLEANING</div>
        <div class="service-tile service-tile--pink">EXIT CLEANS</div>
        <div class="service-tile service-tile--gold">ONE-OFF<br>SEASONAL/<br>PARTY/<br>BUILDING<br>WORK CLEANS</div>
        <div class="service-tile service-tile--blush">LAUNDRY<br>AND<br>IRONING</div>
        <div class="service-tile service-tile--blush">CHIC AND<br>CONTEMPORARY<br>FLOWER<br>ARRANGEMENTS</div>
        <div class="service-tile service-tile--gold">CAR VALETING</div>
        <div class="service-tile service-tile--charcoal">PET FOOD<br>DELIVERY</div>
        <div class="service-tile service-tile--pink">DRY CLEANING</div>
      </div>
      <div class="wardrobe-photo" role="img" aria-label="Photograph of a woman relaxing in a tidy walk-in wardrobe"></div>
      <h3 class="coverage-band">WE LOOK AFTER OUR CLIENTS' HOMES AND HOLIDAY LETS<br>ACROSS SOUTH SOMERSET.</h3>
      <div class="contact">
        <p class="contact-lead">Contact us to arrange a home visit and quotation</p>
        <p class="contact-lines">E: info@hollowmerefarm-example.co.uk<span class="contact-divider">|</span>T: 07700 900417<br>www.hollowmerefarm-example.co.uk</p>
      </div>
    </section>
  </article>
</div>
</body>
</html>
```